Web Design Job: Facial Surgery Center (Velantra)--Web Design Needed

We need a web design for Velantra Facial Surgery. Velantra is in Chesterfield, MO (suburb of St. Louis), and is owned by a double board certified facial plastic surgeon and ENT. The website must feature a before and after photo book, a section for patient reviews, drop down menus that outline services offered (one for surgical procedures and one for office/nonsurgical procedures), and "About the Practice" section, a section to talk about the doctor and his staff, a "What's New" section, a section for information for out of town patients, as well as a link to the Medical Spa also owned by the doctor, as well as Facebook and Twitter. We are open to ideas regarding adding a "tour of the surgery center", featuring video footage of the state of the art facility, as well as other video options. We prefer soothing colors such as aquas and blues, light greys, chocolate browns, etc (does not have to follow the color scheme in the attached logo). We would like the design to be easy to digest and informative, but not "thick". It should be an upscale, classy design that will appeal to all age brackets, but especially middle-aged women, as that is the primary clientele.

Target Market(s)

Middle aged women are our most common client, however, younger patients, both male and female, will often visit the site for select procedures.

Industry/Entity Type

Medical

Number of Pages Required

5+ page

Font styles to use
Sans Serif

Colors
86cfc6
85cae6
cee9f5
cfeae6
edf8f6
85acd3
cfdfed

Requirements
Must have
• Before and after picture book, links to Facebook, Twitter and Instagram, a soothing, peaceful aesthetic, a page for reviews, as well as a link to reviews on Yelp or similar page.
Nice to have
• Drop down menus that include the surgical and nonsurgical procedures. Each surgical procedure could have it's own section that includes a before and after picture book.
Should not have
• Too many words!

```html
<!DOCTYPE html>
<html lang="en">
<head>
<meta charset="utf-8">
<title>Velantra Facial Surgery</title>
<link href="https://fonts.googleapis.com/css2?family=Open+Sans:wght@400;600;700&display=swap" rel="stylesheet">
<style>
:root{
  --teal:#86cfc6;
  --teal-dark:#6fbfb5;
  --teal-pale:#cfeae6;
  --mint:#edf8f6;
  --sky:#cee9f5;
  --ink:#1c1c1c;
  --white:#ffffff;
  --cream:#fbfaf6;
  --black:#050505;
}
*{margin:0;padding:0;box-sizing:border-box}
html,body{width:1200px;height:4800px;overflow:hidden}
body{font-family:"Open Sans",Arial,sans-serif;color:var(--ink);background:var(--white);position:relative}
.abs{position:absolute}
.btn{position:absolute;background:var(--white);color:var(--teal-dark);font-weight:600;font-size:15px;letter-spacing:1px;text-transform:uppercase;text-align:center;border:2px solid var(--teal-pale);white-space:nowrap}

/* top bar */
.topbar{top:0;left:0;width:1200px;height:92px;background:var(--white)}
.topbar .call{left:122px;top:38px;font-size:15px;font-weight:600}
.topbar .follow{left:868px;top:38px;font-size:15px;font-weight:600}
.topbar .dots{left:990px;top:40px;display:flex;gap:10px}
.topbar .dots span{width:16px;height:16px;border-radius:50%;background:var(--ink)}

/* nav */
.nav{top:92px;left:0;width:1200px;height:90px;background:var(--cream)}
.brand{left:150px;top:16px;color:#4b8fb0;font-size:34px;font-weight:600;line-height:1}
.brand-sub{left:158px;top:56px;color:#4b8fb0;font-size:10px;letter-spacing:3px;font-weight:600}
.menu{left:482px;top:34px;display:flex;gap:34px;font-size:15px;font-weight:600;letter-spacing:.5px}
.menu .active{color:var(--teal-dark)}
.dropdown{left:586px;top:182px;width:224px;height:106px;background:var(--teal);padding:16px 0 0 6px;font-size:15px;font-weight:600;line-height:34px;z-index:3}

/* hero */
.hero{top:182px;left:0;width:1200px;height:576px;background:linear-gradient(90deg,#eef0fb 0%,#e6ebfa 55%,#dde4f4 100%)}
.hero-photo{left:680px;top:0;width:520px;height:576px;background:linear-gradient(90deg,#e6ebfa 0%,#e9d6cc 45%,#d9b7a6 100%)}
.arrow{top:222px}
.hero h1{left:157px;top:265px;width:440px;color:var(--teal);font-size:44px;font-weight:600;line-height:46px;letter-spacing:1px}
.hero p{left:157px;top:370px;width:480px;font-size:16px;line-height:22px}
.hero .btn{left:190px;top:448px;width:250px;height:52px;line-height:48px}

/* services */
.services{top:758px;left:0;width:1200px;height:800px;background:var(--teal)}
.section-title{position:absolute;left:0;width:1200px;text-align:center;font-size:44px;font-weight:600;letter-spacing:2px}
.lede{position:absolute;left:0;width:1200px;text-align:center;font-size:16px;line-height:24px}
.services .section-title{top:30px;color:var(--white)}
.services .lede{top:110px;color:var(--white)}
.card{top:224px;width:227px;height:516px;background:var(--teal-pale);border:2px solid var(--white)}
.card .pic{height:244px;width:100%}
.card h3{text-align:center;font-size:20px;font-weight:700;margin-top:12px}
.card p{font-size:16px;line-height:21px;padding:14px 18px 0}
.card .btn{left:56px;bottom:22px;width:112px;height:40px;line-height:36px;font-size:14px;text-transform:none;letter-spacing:.5px}

/* gallery */
.gallery{top:1558px;left:0;width:1200px;height:1216px;background:linear-gradient(90deg,#f6ece6 0%,#fbf5f1 50%,#f4e7df 100%)}
.gallery .section-title{top:30px;color:var(--ink)}
.gallery .lede{top:104px;color:var(--ink)}
.strip{left:128px;top:180px;width:950px;height:320px;background:var(--white);border:1px solid #ddd}
.strip .lbl{position:absolute;top:4px;font-size:12px;font-weight:600;line-height:14px}
.strip .lbl small{display:block;font-weight:400;font-size:9px;line-height:11px}
.strip .shot{position:absolute;top:36px;width:226px;height:252px}

/* doctors */
.doctors{top:2774px;left:0;width:1200px;height:784px;background:var(--teal)}
.doctors .section-title{top:28px;color:var(--white)}
.doc{top:186px;width:330px;text-align:center;color:var(--white)}
.doc .avatar{width:276px;height:276px;margin:0 auto;border-radius:50%;border:8px solid var(--white)}
.doc h4{font-size:22px;font-weight:700;letter-spacing:1px;margin-top:12px}
.doc .years{font-size:22px;font-weight:600;letter-spacing:1px}
.doc q{display:block;font-size:16px;line-height:24px;width:250px;margin:18px auto 0}
.doctors .btn{left:506px;top:692px;width:188px;height:64px;line-height:60px;font-size:20px}

/* reviews */
.reviews{top:3558px;left:0;width:1200px;height:516px;background:var(--white)}
.reviews .section-title{top:44px;color:var(--ink)}
.reviews .lede{top:114px;left:200px;width:800px}
.stat{top:218px;width:218px;height:224px;background:var(--teal);color:var(--white);text-align:center;border:3px solid var(--white);box-shadow:0 10px 14px rgba(0,0,0,.25)}
.stat .ico{width:104px;height:104px;border-radius:50%;background:var(--white);margin:14px auto 0;display:flex;align-items:center;justify-content:center}
.stat .num{font-size:44px;font-weight:600;margin-top:6px;letter-spacing:2px;line-height:52px}
.stat .lab{font-size:20px;font-weight:700;letter-spacing:1px}

/* location */
.location{top:4074px;left:0;width:1200px;height:390px;background:var(--white)}
.map{left:122px;top:4px;width:508px;height:378px;background:linear-gradient(135deg,#e8ece4 0%,#dfe6dc 55%,#d6dde3 100%)}
.loc-panel{left:630px;top:0;width:570px;height:390px;background:var(--teal);color:var(--white);padding:14px 0 0 18px}
.loc-panel h2{font-size:44px;font-weight:600;letter-spacing:2px}
.loc-rule{width:552px;border-top:2px dashed var(--white)}
.loc-panel .addr{font-size:20px;line-height:26px;margin-top:20px;width:500px}
.loc-panel .phone{font-size:20px;font-weight:700;margin-top:6px}
.loc-panel .btn{left:18px;top:226px;width:192px;height:50px;line-height:46px;font-size:15px}

/* footer */
.footer{top:4464px;left:0;width:1200px;height:336px;background:var(--black);color:var(--white)}
.fcol{top:28px;width:300px}
.fcol h5{font-size:30px;font-weight:700;letter-spacing:1px}
.fcol p{font-size:16px;line-height:22px;margin-top:24px;width:240px}
.fcol .btn{position:static;display:block;width:98px;height:36px;line-height:32px;font-size:14px;margin-top:16px;color:var(--ink)}
.fcol ul{list-style:none;margin-top:20px;font-size:16px;line-height:24px}
.fcol li:before{content:"";display:inline-block;width:8px;height:8px;background:var(--white);margin-right:12px;vertical-align:middle}
</style>
</head>
<body>

<header class="topbar abs">
  <div class="call abs">Call Now: &nbsp;(0800)555-019</div>
  <div class="follow abs">Follow Us:</div>
  <div class="dots abs"><span></span><span></span><span></span><span></span></div>
</header>

<nav class="nav abs">
  <div class="brand abs">Velantra</div>
  <div class="brand-sub abs">FACIAL SURGERY</div>
  <div class="menu abs">
    <span>HOME</span><span class="active">SERVICES</span><span>BEFORE/AFTER</span><span>GALLERY</span><span>CONTACT</span>
  </div>
</nav>

<div class="dropdown abs">
  <div>Surgical Procedures</div>
  <div>Nonsurgical Procedures</div>
</div>

<section class="hero abs">
  <div class="hero-photo abs" role="img" aria-label="Portrait photograph of a woman with smooth skin, half retouched"></div>
  <svg class="arrow abs" style="left:118px" width="24" height="40" viewBox="0 0 24 40"><path d="M18 6 L6 20 L18 34" fill="none" stroke="#111" stroke-width="4"/></svg>
  <svg class="arrow abs" style="left:1058px" width="24" height="40" viewBox="0 0 24 40"><path d="M6 6 L18 20 L6 34" fill="none" stroke="#111" stroke-width="4"/></svg>
  <h1 class="abs">The Art of Looking Beautiful.</h1>
  <p class="abs">The most common breast lift operation, called mastopexy, repositions the nipple higher on the chest wall.</p>
  <div class="btn">Make an Appointment</div>
</section>

<section class="services abs">
  <h2 class="section-title">What We Offer Cosmatic Procedures</h2>
  <p class="lede">I am so happy, my dear friend, so absorbed in the exquisite sense of<br>mere tranquil existence, that I neglect my talents.</p>

  <article class="card abs" style="left:125px">
    <div class="pic" role="img" aria-label="Photo of a woman receiving a skin treatment" style="background:linear-gradient(160deg,#f3e6df,#d9b9a8)"></div>
    <h3>Hair &amp; Skin</h3>
    <p>Skin &amp; Hair estibulum sed erat ultricies, volutpat orci sed, vestibulum mauris.</p>
    <div class="btn">Read More</div>
  </article>
  <article class="card abs" style="left:368px">
    <div class="pic" role="img" aria-label="Photo of a woman receiving a facial injection" style="background:linear-gradient(160deg,#b7dfe0,#c9a6c8)"></div>
    <h3>Head &amp; Face</h3>
    <p>Head &amp; Face desktop publishing packages and web page editors ipsumsimpl their web sisimple dummy.</p>
    <div class="btn">Read More</div>
  </article>
  <article class="card abs" style="left:611px">
    <div class="pic" role="img" aria-label="Photo of a man having his face examined" style="background:linear-gradient(160deg,#f1ece8,#c9a08a)"></div>
    <h3>For Men</h3>
    <p>Today, men of all ages and all walks of life are requesting plastic surgery for cosmetic reasons.</p>
    <div class="btn">Read More</div>
  </article>
  <article class="card abs" style="left:851px">
    <div class="pic" role="img" aria-label="Photo of a marked torso before body treatment" style="background:linear-gradient(160deg,#ede4df,#d8b6a3)"></div>
    <h3>Body Treatment</h3>
    <p>Vivamus laoreet feugiat tortor, non euismod ipsum facilisis in. Aliquam arcu sapien, ultricies sollicitudin elit et, ornare facilisis orci.</p>
    <div class="btn">Read More</div>
  </article>
</section>

<section class="gallery abs">
  <h2 class="section-title">Gallery Before / After</h2>
  <p class="lede">I am so happy, my dear friend, so absorbed in the exquisite sense of<br>mere tranquil existence, that I neglect my talents.</p>

  <div class="strip abs">
    <span class="lbl" style="left:6px">Before treatment<small>no photos retouched</small></span>
    <span class="lbl" style="left:246px">Session 2 results</span>
    <span class="lbl" style="left:486px">Session 3 results</span>
    <span class="lbl" style="left:726px">Month 7 after first injection results</span>
    <div class="shot" style="left:6px;background:linear-gradient(180deg,#c9a27a,#dcb8a0)" role="img" aria-label="Before photo of a blonde woman"></div>
    <div class="shot" style="left:246px;background:linear-gradient(180deg,#c9a27a,#dcb8a0)" role="img" aria-label="Session 2 result photo"></div>
    <div class="shot" style="left:486px;background:linear-gradient(180deg,#c9a27a,#dcb8a0)" role="img" aria-label="Session 3 result photo"></div>
    <div class="shot" style="left:726px;background:linear-gradient(180deg,#c9a27a,#dcb8a0)" role="img" aria-label="Month 7 result photo"></div>
  </div>

  <div class="abs" style="left:186px;top:522px;width:390px;height:253px;background:linear-gradient(90deg,#3a2a22,#c89d86 50%,#3a2a22)" role="img" aria-label="Before and after photos of a dark haired woman"></div>
  <div class="abs" style="left:630px;top:522px;width:368px;height:253px;background:linear-gradient(90deg,#8fcfc7,#b7a79c 50%,#8fcfc7)" role="img" aria-label="Before and after photos of an older man with a zoom icon"></div>
  <div class="abs" style="left:250px;top:797px;width:326px;height:371px;background:linear-gradient(180deg,#f4f4f4,#e3cfc3 50%,#f4f4f4)" role="img" aria-label="Front and profile before and after photos of a young woman"></div>
  <div class="abs" style="left:630px;top:797px;width:336px;height:371px;background:linear-gradient(180deg,#f4f4f4,#e3cfc3 50%,#f4f4f4)" role="img" aria-label="Front and profile before and after photos of a second woman"></div>
</section>

<section class="doctors abs">
  <h2 class="section-title">Experienced Doctors</h2>
  <div class="doc abs" style="left:110px">
    <div class="avatar" role="img" aria-label="Portrait of Dr. Harlow in a white coat" style="background:linear-gradient(180deg,#dfe6ea,#c7d3da)"></div>
    <h4>DR. HARLOW</h4><div class="years">Practicing for 20 years</div>
    <q>A wonderful serenity has taken possession of my entire soul, like these sweet mornings of spring which I enjoy with my whole heart.</q>
  </div>
  <div class="doc abs" style="left:443px">
    <div class="avatar" role="img" aria-label="Portrait of Dr. Quinn in a white coat" style="background:linear-gradient(180deg,#e8dfd8,#c9b2a4)"></div>
    <h4>DR. QUINN</h4><div class="years">Practicing for 23 years</div>
    <q>A wonderful serenity has taken possession of my entire soul, like these sweet mornings of spring which I enjoy with my whole heart.</q>
  </div>
  <div class="doc abs" style="left:773px">
    <div class="avatar" role="img" aria-label="Portrait of Dr. Mercer in a white coat" style="background:linear-gradient(180deg,#dfe6ea,#c4b6ac)"></div>
    <h4>DR. MERCER</h4><div class="years">Practicing for 25 years</div>
    <q>A wonderful serenity has taken possession of my entire soul, like these sweet mornings of spring which I enjoy with my whole heart.</q>
  </div>
  <div class="btn">View Staff</div>
</section>

<section class="reviews abs">
  <h2 class="section-title">Patient Reviews</h2>
  <p class="lede">Lorem ipsum dolor sit amet, ei est iisque aliquid, dolore omnium principes eos at, fabulas accusam scribentur ei cum. Ne ius mucius gloriatur scripserit, tation partem tempor et eos. Ne vix nostro theophrastus. Eum ad illud delenit reprehendunt.</p>

  <div class="stat abs" style="left:141px">
    <div class="ico"><svg width="60" height="60" viewBox="0 0 60 60" fill="none" stroke="#111" stroke-width="5"><path d="M14 8 v18 a12 12 0 0 0 24 0 V8"/><path d="M26 38 v6 a10 10 0 0 0 20 0 v-8"/><circle cx="46" cy="30" r="5"/></svg></div>
    <div class="num">135</div><div class="lab">Doctors</div>
  </div>
  <div class="stat abs" style="left:378px">
    <div class="ico"><svg width="60" height="60" viewBox="0 0 60 60" fill="#111"><path d="M14 12 h32 l-4 14 H18z"/><circle cx="30" cy="34" r="10"/><path d="M12 58 a18 14 0 0 1 36 0z"/><rect x="28" y="14" width="4" height="10" fill="#fff"/><rect x="25" y="17" width="10" height="4" fill="#fff"/></svg></div>
    <div class="num">600</div><div class="lab">Nurses</div>
  </div>
  <div class="stat abs" style="left:611px">
    <div class="ico"><svg width="60" height="60" viewBox="0 0 60 60" fill="#111"><rect x="6" y="10" width="48" height="22" rx="3"/><rect x="26" y="13" width="8" height="16" fill="#fff"/><rect x="22" y="17" width="16" height="8" fill="#fff"/><rect x="4" y="36" width="52" height="10"/><rect x="6" y="46" width="6" height="8"/><rect x="48" y="46" width="6" height="8"/></svg></div>
    <div class="num">1,000</div><div class="lab">Rooms</div>
  </div>
  <div class="stat abs" style="left:845px">
    <div class="ico"><svg width="60" height="60" viewBox="0 0 60 60" fill="#111"><circle cx="22" cy="10" r="6"/><rect x="14" y="18" width="16" height="22" rx="3"/><rect x="15" y="40" width="6" height="16"/><rect x="23" y="40" width="6" height="16"/><circle cx="40" cy="22" r="5"/><rect x="34" y="29" width="12" height="16" rx="3"/><rect x="35" y="45" width="4" height="11"/><rect x="41" y="45" width="4" height="11"/></svg></div>
    <div class="num">10,000</div><div class="lab">Patients</div>
  </div>
</section>

<section class="location abs">
  <div class="map abs" role="img" aria-label="Street map showing the clinic location"></div>
  <div class="loc-panel abs">
    <h2>Location:</h2>
    <div class="loc-rule"></div>
    <p class="addr">2400 Linden Way # 210, Brookhaven Glen, MO 63190, United States</p>
    <p class="phone">(0800)555-019</p>
    <div class="btn">Get Directions</div>
  </div>
</section>

<footer class="footer abs">
  <div class="fcol abs" style="left:122px">
    <h5>About Us</h5>
    <p>Lorem ipsum dolor sit amet, ei est iisque aliquid, dolore omnium principes eos at,fabulas accusam scribentur ei cum</p>
    <span class="btn">MORE</span>
  </div>
  <div class="fcol abs" style="left:464px">
    <h5>What's New</h5>
    <p>Lorem ipsum dolor sit amet, ei est iisque aliquid, dolore omnium principes eos at,fabulas accusam scribentur ei cum</p>
    <span class="btn">MORE</span>
  </div>
  <div class="fcol abs" style="left:800px">
    <h5>Quick Links</h5>
    <ul><li>About us</li><li>Treatments</li><li>Before/After</li><li>Doctor's</li><li>FAQ's</li></ul>
  </div>
</footer>

</body>
</html>
```